Amber Hollow Business Card and Logo

Nutrition and Wellness Store Front. I sell supplements, herbs, tinctures, Loose Leaf Teas, natural snacks and drinks including gluten free. classes: Fitness; health and wellness; community health and wellness hub. It is a "shabby chic" store front. It is white and my accent color is turqouise I will be adding some jewelry, stones and rocks and jewelery. I am a Certified Herbalist and Certified Nutrition and Wellness Consultant, a Vosari Practitioner and Kaloro instructor.

Target Market(s)

health and wellness seekers, fitness, baby boomer

Industry/Entity Type

Business

Contact Information for Business Card

Amber Hollow Nutrition and Wellness
Linda Marcovitch Certified Herbalist , Certified Nutrition and Wellness Consultant, Vosari Practitioner, Kaloro Instructor

Font styles to use
Serif

Colors
33a6d7
3176b5
33b8a4

Requirements
Must have
• A picture that represents two mountain peaks with a floral accent.

```html
<!DOCTYPE html>
<html lang="en">
<head>
<meta charset="utf-8">
<title>Amber Hollow Nutrition and Wellness – Business Card</title>
<link rel="stylesheet" href="https://fonts.googleapis.com/css2?family=Cormorant+Garamond:wght@500&family=Open+Sans:wght@300;400;700&display=swap">
<style>
  :root {
    --page-bg: #ecebe8;
    --card-white: #ffffff;
    --card-shade: #eef0f2;
    --accent-blue: #3a97c8;
    --accent-sky: #33a6d7;
    --accent-deep: #3176b5;
    --accent-teal: #33b8a4;
    --text-light: #ffffff;
  }
  html, body {
    margin: 0;
    padding: 0;
    width: 1200px;
    height: 1022px;
    overflow: hidden;
    background: var(--page-bg);
  }
  .stage {
    position: relative;
    width: 1200px;
    height: 1022px;
  }
  .business-card {
    position: absolute;
    left: 100px;
    top: 225px;
    width: 1000px;
    height: 572px;
    border-radius: 26px;
    overflow: hidden;
    background: linear-gradient(135deg, var(--card-white) 40%, var(--card-shade) 100%);
    box-shadow: 0 18px 40px rgba(0,0,0,0.18);
  }
  .card-art {
    position: absolute;
    inset: 0;
    width: 1000px;
    height: 572px;
  }
  .brand {
    position: absolute;
    left: 40px;
    top: 250px;
    width: 360px;
    display: flex;
    align-items: center;
    gap: 16px;
    color: var(--text-light);
    font-family: "Cormorant Garamond", Georgia, serif;
    font-weight: 500;
    font-size: 36px;
    line-height: 1.1;
  }
  .brand-dot {
    flex: 0 0 auto;
    width: 42px;
    height: 42px;
    border-radius: 50%;
    background: var(--text-light);
  }
  .details {
    position: absolute;
    right: 56px;
    top: 150px;
    text-align: right;
    font-family: "Open Sans", Arial, sans-serif;
  }
  .person-name {
    margin: 0;
    font-weight: 700;
    font-size: 44px;
    color: var(--accent-blue);
    letter-spacing: 0.5px;
  }
  .credential-list {
    list-style: none;
    margin: 10px 0 0;
    padding: 0;
  }
  .credential {
    font-weight: 400;
    font-size: 24px;
    line-height: 1.5;
    color: var(--accent-deep);
  }
  .credential-lead {
    color: var(--accent-sky);
    margin-bottom: 44px;
  }
  .tick {
    display: inline-block;
    width: 20px;
    height: 16px;
    margin-left: 10px;
    vertical-align: 0;
  }
</style>
</head>
<body>
<div class="stage">
  <div class="business-card">
    <svg class="card-art" viewBox="0 0 1000 572">
      <defs>
        <linearGradient id="scene-tones" x1="0" y1="0" x2="0.6" y2="1">
          <stop offset="0" stop-color="#c9d6e4"/>
          <stop offset="0.22" stop-color="#6f5a52"/>
          <stop offset="0.45" stop-color="#3f5e3a"/>
          <stop offset="0.65" stop-color="#7a5bb0"/>
          <stop offset="0.85" stop-color="#4e7f35"/>
          <stop offset="1" stop-color="#6a9a3f"/>
        </linearGradient>
      </defs>
      <path role="img" aria-label="Photograph of two snowy mountain peaks above a meadow of purple lupine flowers"
            d="M0 0 H460 C600 140 380 300 400 572 H0 Z" fill="url(#scene-tones)"/>
      <path d="M460 0 C600 140 380 300 400 572" fill="none" stroke="#3a97c8" stroke-width="9"/>
    </svg>

    <div class="brand">
      <span class="brand-dot"></span>
      <span class="brand-name">Amber Hollow Nutrition and Wellness</span>
    </div>

    <div class="details">
      <h1 class="person-name">Linda Marcovitch</h1>
      <ul class="credential-list">
        <li class="credential credential-lead">Certified Herbalist<svg class="tick" viewBox="0 0 22 18"><path d="M2 9 L8 15 L20 3" fill="none" stroke="#33b8a4" stroke-width="3.5" stroke-linecap="round" stroke-linejoin="round"/></svg></li>
        <li class="credential">Vosari Practitioner<svg class="tick" viewBox="0 0 22 18"><path d="M2 9 L8 15 L20 3" fill="none" stroke="#33b8a4" stroke-width="3.5" stroke-linecap="round" stroke-linejoin="round"/></svg></li>
        <li class="credential">Kaloro Instructor<svg class="tick" viewBox="0 0 22 18"><path d="M2 9 L8 15 L20 3" fill="none" stroke="#33b8a4" stroke-width="3.5" stroke-linecap="round" stroke-linejoin="round"/></svg></li>
        <li class="credential">Certified Nutrition and Wellness Consultant</li>
      </ul>
    </div>
  </div>
</div>
</body>
</html>
```